Selka Marrow Photography Business Card

I need a new business card/ possibly design to use for other marking materials ... I have included my logo below in a few different colors, but can also provide the logo in additional colors and sizes. I would love a card the expresses clean, simple and classy.

Target Market(s)

Portrait photography clients, child photography clients

Industry/Entity Type

Photographer

Contact Information for Business Card

Selka Marrow Photography, Fernbrook MA, www.selkamarrowphotography.example
T. 555-283-9146 E. selkamarrowphoto@mailbox.example

Colors
33b8a4
eea4c8
5c5c5c

Requirements
Must have
• I would like to include my logo on card.
Nice to have
• I also like the color brown as well as the choices below. I would like a simple, elegant card, something classy.

```html
<!DOCTYPE html>
<html lang="en">
<head>
<meta charset="utf-8">
<title>Selka Marrow Photography – Business Card</title>
<link rel="stylesheet" href="https://fonts.googleapis.com/css2?family=Montserrat:wght@400;500;600;700&display=swap">
<style>
  :root {
    --page: #ececec;
    --card: #2a2a2a;
    --card-shade: #323232;
    --band: #0b0b0b;
    --ink: #ffffff;
    --ink-soft: #d8d8d8;
    --photo-warm-a: #5d6b35;
    --photo-warm-b: #a7a17a;
    --photo-soft-a: #6f6a52;
    --photo-soft-b: #d9cbb2;
  }
  * { box-sizing: border-box; margin: 0; padding: 0; }
  html, body { width: 1200px; height: 750px; overflow: hidden; }
  body {
    background: var(--page);
    font-family: "Montserrat", sans-serif;
    color: var(--ink);
    position: relative;
  }
  .card {
    position: absolute;
    width: 540px;
    height: 310px;
    border-radius: 22px;
    overflow: hidden;
    background: var(--card);
    box-shadow: 0 14px 30px rgba(0,0,0,0.28);
  }
  .card--front { left: 40px; top: 220px; }
  .card--back { left: 620px; top: 220px; }
  .card svg.shapes { position: absolute; inset: 0; }

  /* front */
  .brand {
    position: absolute;
    left: 262px; width: 270px; top: 96px;
    text-align: center;
  }
  .brand-mark {
    width: 34px; height: 34px; border-radius: 50%;
    background: var(--ink);
    margin: 0 auto 14px;
  }
  .brand-name {
    font-size: 19px; font-weight: 400; letter-spacing: 1px;
    color: var(--ink);
    line-height: 1.3;
  }
  .brand-sub {
    font-size: 8px; font-weight: 400; letter-spacing: 3px;
    color: var(--ink);
    margin-top: 2px;
  }
  .site-band {
    position: absolute;
    left: 258px; right: 0; top: 248px; height: 32px;
    padding: 0 10px;
    display: flex; align-items: center; justify-content: center;
    font-size: 9.5px; font-weight: 700; letter-spacing: 0.2px;
    white-space: nowrap;
    color: var(--ink);
  }

  /* back */
  .identity {
    position: absolute;
    left: 36px; top: 140px;
  }
  .identity-name {
    font-size: 26px; font-weight: 700; letter-spacing: 0.5px; line-height: 1;
  }
  .identity-role {
    font-size: 11px; font-weight: 600; letter-spacing: 1.5px;
    text-align: right; margin-top: 4px;
  }
  .contacts {
    position: absolute;
    left: 0; top: 196px;
    list-style: none;
  }
  .contact {
    display: flex; align-items: center;
    height: 24px; margin-bottom: 3px;
    font-size: 12px; font-weight: 500; color: var(--ink-soft);
  }
  .contact-icon {
    width: 38px; height: 24px;
    background: var(--band);
    border-radius: 0 12px 12px 0;
    display: flex; align-items: center; justify-content: center;
    margin-right: 14px;
  }
  .contact-icon svg { width: 13px; height: 13px; }
</style>
</head>
<body>

  <section class="card card--front">
    <svg class="shapes" viewBox="0 0 540 310" width="540" height="310">
      <defs>
        <linearGradient id="front-photo-tone" x1="0" y1="0" x2="1" y2="1">
          <stop offset="0" stop-color="var(--photo-warm-a)"/>
          <stop offset="1" stop-color="var(--photo-warm-b)"/>
        </linearGradient>
      </defs>
      <polygon class="panel-shade" points="250,0 330,0 270,310 258,310" fill="var(--card-shade)"/>
      <polygon class="front-photo" role="img" aria-label="Photo of two small children with a red tricycle in a sunny garden"
               points="0,0 248,0 262,310 0,310" fill="url(#front-photo-tone)"/>
      <rect class="band" x="258" y="248" width="282" height="32" fill="var(--band)"/>
    </svg>
    <div class="brand">
      <div class="brand-mark"></div>
      <p class="brand-name">Selka Marrow</p>
      <p class="brand-sub">PHOTOGRAPHY</p>
    </div>
    <p class="site-band">WWW.SELKAMARROWPHOTOGRAPHY.EXAMPLE</p>
  </section>

  <section class="card card--back">
    <svg class="shapes" viewBox="0 0 540 310" width="540" height="310">
      <defs>
        <linearGradient id="back-photo-tone" x1="0" y1="0" x2="1" y2="1">
          <stop offset="0" stop-color="var(--photo-soft-a)"/>
          <stop offset="1" stop-color="var(--photo-soft-b)"/>
        </linearGradient>
      </defs>
      <polygon class="panel-shade" points="120,118 300,40 540,250 420,310" fill="var(--card-shade)"/>
      <polygon class="back-photo" role="img" aria-label="Photo of a smiling little girl in a floral dress sitting outdoors"
               points="190,0 540,0 540,190 150,95" fill="url(#back-photo-tone)"/>
      <polygon class="corner" points="480,0 540,0 540,30" fill="var(--band)"/>
    </svg>

    <div class="identity">
      <h1 class="identity-name">SELKA MARROW</h1>
      <p class="identity-role">PHOTOGRAPHER</p>
    </div>

    <ul class="contacts">
      <li class="contact">
        <span class="contact-icon">
          <svg viewBox="0 0 16 16"><path d="M4 1.5l2.3 3-1.4 1.6c.8 1.8 2.2 3.2 4 4l1.6-1.4 3 2.3-1.2 2.6C7 13.3 2.7 9 1.4 2.7z" fill="#fff"/></svg>
        </span>555-283-9146
      </li>
      <li class="contact">
        <span class="contact-icon">
          <svg viewBox="0 0 16 16"><rect x="1.5" y="3.5" width="13" height="9" fill="none" stroke="#fff" stroke-width="1.4"/><path d="M1.5 3.5l6.5 5 6.5-5" fill="none" stroke="#fff" stroke-width="1.4"/></svg>
        </span>selkamarrowphoto@mailbox.example
      </li>
      <li class="contact">
        <span class="contact-icon">
          <svg viewBox="0 0 16 16"><circle cx="8" cy="8" r="6.3" fill="none" stroke="#fff" stroke-width="1.4"/><ellipse cx="8" cy="8" rx="2.6" ry="6.3" fill="none" stroke="#fff" stroke-width="1.2"/><path d="M1.7 8h12.6" stroke="#fff" stroke-width="1.2"/></svg>
        </span>www.selkamarrowphotography.example
      </li>
      <li class="contact">
        <span class="contact-icon">
          <svg viewBox="0 0 16 16"><path d="M8 15s-5-5.3-5-8.8A5 5 0 0 1 13 6.2C13 9.7 8 15 8 15z" fill="#fff"/><circle cx="8" cy="6.2" r="1.9" fill="#0b0b0b"/></svg>
        </span>Fernbrook MA
      </li>
    </ul>
  </section>

</body>
</html>
```